Business software developers new website

We need to redesign our website. Our current website is http://www.quorvanta.net/index.html, which is outdated and needs a new look. We moved out from web design and have concentrated more on the back end of the systems, for example, system support and security and cloud-based applications. Our major clients include both private and government sectors. We would like to see some designs that are all in one page, simple and clean. Prefer illustrator or obstructed images instead of real-life photos. Must look futuristic yet friendly. Attached the new logo for your references and good luck.

Target Market(s)

Medium to big company for their IT or data management. Either improve or upgrade their current system.

Industry/Entity Type

Business Software

Number of Pages Required

1 page

Colors

Designer to choose colors to be used in the design.

Requirements
Must have
• Simple and clean. Individual assets must be provided in the correct size and format(png or jpeg). Prefer Goggle fonts. Even though the logo color is red, grey and black, still prefer some modern colors that go well with red. When design, must consider the possibility to convert it into responsive.
Nice to have
• White background
Should not have
• real life photos, no slider

```html
<!DOCTYPE html>
<html lang="en">
<head>
<meta charset="utf-8">
<title>quorvanta.net — System Support, Security and Cloud</title>
<link rel="stylesheet" href="https://fonts.googleapis.com/css2?family=Roboto+Condensed:wght@300;400;700&family=Jost:wght@400;500&display=swap">
<style>
:root{
  --red:#e8313a;
  --ink:#1f1f1f;
  --text:#555;
  --muted:#8a8a8a;
  --grey-band:#f4f4f4;
  --line:#e3e3e3;
  --footer:#2b2b2b;
  --white:#fff;
  --sky:#dff1fb;
  --blue:#2f7fd6;
}
*{box-sizing:border-box;margin:0;padding:0}
html,body{width:1200px;height:4096px;overflow:hidden}
body{position:relative;background:var(--white);font-family:'Jost',sans-serif;color:var(--text)}
.abs{position:absolute}
.head{font-family:'Roboto Condensed',sans-serif;font-weight:700;color:var(--ink);letter-spacing:-.2px}
.head em{font-style:normal;color:var(--red)}
.mark{display:block;width:14px;height:14px;border-radius:50%;background:var(--red);margin-top:10px}
.rule{display:flex;align-items:center;gap:0;margin-top:8px}
.rule .mark{margin:0}
.rule::before,.rule::after{content:"";height:1px;width:90px;background:var(--line)}
.centered{display:flex;flex-direction:column;align-items:center}
.btn{display:inline-flex;align-items:center;gap:10px;height:34px;padding:0 18px 0 6px;border-radius:0 17px 17px 0;background:var(--red);color:var(--white);font-size:13px;font-weight:500;border-radius:8px 17px 17px 8px}
.btn::before{content:"";width:22px;height:22px;border-radius:50%;background:var(--white)}
.social{display:flex;gap:8px}
.social span{width:22px;height:22px;border-radius:50%;background:var(--red)}
p.body{font-size:13px;line-height:25.5px;text-align:justify}

/* top bar & nav */
.topbar{left:0;top:0;width:1200px;height:45px}
.topbar .contact{left:141px;top:13px;display:flex;gap:26px;font-size:14px;color:var(--ink)}
.topbar .contact span{display:flex;align-items:center;gap:8px}
.topbar .social{left:972px;top:11px}
.nav{left:0;top:45px;width:1200px;height:82px;background:#f3f3f3}
.logo{display:flex;align-items:center;gap:8px;font-family:'Jost',sans-serif;font-size:36px;color:var(--ink);letter-spacing:-.5px}
.logo i{width:14px;height:14px;border-radius:50%;background:var(--red)}
.nav .logo{left:141px;top:18px}
.nav ul{list-style:none;right:141px;top:32px;display:flex;gap:34px;font-size:13px;color:var(--ink)}
.nav li.on{color:var(--red);font-weight:500}

/* hero */
.hero-text{left:141px;top:245px}
.hero-text .l1{font-family:'Roboto Condensed',sans-serif;font-weight:300;font-size:36px;color:var(--ink)}
.hero-text .l2{font-size:35px;margin-top:2px}
.hero-text .l3{font-size:24px;margin-top:6px}
.hero-text .btn{margin-top:34px}
.hero-art{left:660px;top:190px;width:334px;height:336px;border-radius:12px;background:radial-gradient(circle at 50% 50%,#cfe6fb 0%,#eaf4fd 55%,#fff 100%)}

/* about */
.about{left:0;top:585px;width:1200px;height:563px;background:var(--grey-band)}
.about .ring{left:142px;top:70px;width:422px;height:422px;border-radius:50%;border:1.5px dashed #f0a5aa}
.about .art{left:170px;top:98px;width:366px;height:366px;border-radius:50%;background:radial-gradient(circle,#d6eefa 0%,var(--sky) 60%,#eef8fd 100%)}
.about .copy{left:653px;top:135px;width:405px}
.about .copy h2{font-size:32px}
.about .copy p{margin-top:20px}
.about .copy .btn{margin-top:20px}

/* clients */
.clients .copy{left:141px;top:1315px;width:402px}
.clients h2{font-size:32px}
.clients p{margin-top:22px}
.clients .btn{margin-top:22px}
.arrow{width:32px;height:32px;border-radius:50%;background:var(--white);box-shadow:0 2px 8px rgba(0,0,0,.15);display:flex;align-items:center;justify-content:center}
.logo-card{width:155px;height:99px;background:var(--white);box-shadow:0 3px 12px rgba(0,0,0,.12);display:flex;align-items:center;justify-content:center;font-family:'Roboto Condensed',sans-serif;font-weight:700;font-size:17px;color:#333;text-transform:uppercase;letter-spacing:1px}

/* services */
.services{left:0;top:1736px;width:1200px;height:439px;background:var(--grey-band)}
.services .title{left:0;top:70px;width:1200px}
.services h2,.news h2,.contact h2{font-size:32px}
.svc{width:170px;text-align:center;font-size:16px;color:var(--ink);line-height:21px}
.svc .disc{width:140px;height:140px;margin:0 auto 18px;border-radius:50%;background:var(--white);box-shadow:0 4px 14px rgba(0,0,0,.12);display:flex;align-items:center;justify-content:center}
.svc.on .disc{border:4px solid var(--red)}

/* news */
.news .title{left:0;top:2238px;width:1200px}
.card{top:2332px;width:287px;height:393px;background:var(--white);border:1px solid #dcdcdc;box-shadow:0 2px 8px rgba(0,0,0,.05);padding:8px}
.card .img{height:168px;position:relative}
.card .date{position:absolute;right:0;top:0;width:36px;height:38px;background:var(--red);color:var(--white);text-align:center;font-size:16px;line-height:16px;padding-top:4px}
.card .date small{display:block;font-size:9px;line-height:11px}
.card h3{font-family:'Jost',sans-serif;font-weight:500;font-size:16px;color:var(--ink);line-height:21px;margin:26px 6px 0}
.card p{font-size:12.5px;line-height:23px;margin:6px 6px 0}
.card .btn{margin:20px 6px 0}

/* faq & philosophy */
.faqband{left:0;top:2798px;width:1200px;height:458px;background:#fafafa}
.faq{left:141px;top:2868px;width:423px}
.faq h2,.philo h2{font-size:32px}
.acc-open{margin-top:30px}
.acc-head{height:41px;display:flex;align-items:center;justify-content:space-between;padding:0 15px;font-size:13px}
.acc-open .acc-head{background:var(--red);color:var(--white)}
.acc-body{background:var(--white);border:1px solid var(--line);border-top:none;padding:10px 15px;font-size:13px;line-height:23px;text-align:justify}
.acc-closed{margin-top:22px;border:1px solid var(--line);background:var(--white);color:var(--ink)}
.acc-closed span:last-child{color:var(--red);font-size:18px}
.divider{left:601px;top:2852px;height:340px;border-left:1px dashed #d3d3d3}
.philo{left:636px;top:2868px;width:423px}
.philo .box{margin-top:30px;background:var(--white);box-shadow:0 4px 20px rgba(0,0,0,.08);padding:20px 20px 22px}
.philo .box .btn{margin-top:18px}

/* contact */
.contact .title{left:0;top:3325px;width:1200px}
.form{left:302px;top:3426px;width:596px;display:grid;grid-template-columns:1fr 1fr;gap:18px 16px}
.field{height:34px;border:1px solid #d8d8d8;padding:0 14px;font-size:11px;color:#777;display:flex;align-items:center;gap:12px}
.field.msg{grid-column:1/3;height:86px;align-items:flex-start;padding-top:12px}
.box-check{width:20px;height:20px;border:1.5px solid #bbb;border-radius:2px}
.contact .send{left:550px;top:3661px}

/* footer */
.footer{left:0;top:3790px;width:1200px;height:306px;background:var(--footer);color:#cfcfcf}
.footer .col{top:76px;font-size:11.5px;line-height:20.5px}
.footer h4{font-family:'Roboto Condensed',sans-serif;font-weight:400;font-size:15px;color:var(--white);letter-spacing:.5px;text-transform:uppercase}
.footer h4 em{font-style:normal;color:var(--red)}
.footer h4::after{content:"";display:block;width:34px;height:2px;background:var(--red);margin:8px 0 14px}
.footer .logo{color:var(--white);font-size:32px}
.footer .row{display:flex;align-items:center;gap:12px;margin-bottom:9px}
.footer .dot{width:9px;height:9px;border-radius:50%;background:var(--red)}
.news-form{display:flex;margin-top:10px;width:282px;height:29px;border-radius:15px;background:var(--white);overflow:hidden}
.news-form span{flex:1;padding:0 14px;color:#888;display:flex;align-items:center}
.news-form b{width:80px;background:var(--red);color:var(--white);font-weight:500;display:flex;align-items:center;justify-content:center;border-radius:15px}
.footer .copy{left:0;top:260px;width:1200px;text-align:center;font-size:12px;border-top:1px solid #444;padding-top:14px}
</style>
</head>
<body>

<header class="abs topbar">
  <div class="abs contact">
    <span><svg width="16" height="16" viewBox="0 0 24 24" fill="none" stroke="#e8313a" stroke-width="2"><path d="M22 16.9v3a2 2 0 0 1-2.2 2 19.8 19.8 0 0 1-8.6-3.1 19.5 19.5 0 0 1-6-6A19.8 19.8 0 0 1 2.1 4.2 2 2 0 0 1 4.1 2h3a2 2 0 0 1 2 1.7c.1.9.4 1.8.7 2.7a2 2 0 0 1-.5 2.1L8 9.8a16 16 0 0 0 6 6l1.3-1.3a2 2 0 0 1 2.1-.5c.9.3 1.8.6 2.7.7a2 2 0 0 1 1.7 2z"/></svg>+61 7 5550 1842</span>
    <span><svg width="16" height="14" viewBox="0 0 24 20" fill="none" stroke="#e8313a" stroke-width="2"><rect x="1" y="1" width="22" height="18" rx="2"/><path d="M1 3l11 8 11-8"/></svg>info@quorvanta.com</span>
  </div>
  <div class="abs social" aria-label="Social links"><span></span><span></span><span></span></div>
</header>

<nav class="abs nav">
  <div class="abs logo">quorvanta.net<i></i></div>
  <ul class="abs"><li class="on">Home</li><li>Our Services</li><li>Our Clients</li><li>Contact Us</li></ul>
</nav>

<section class="hero">
  <div class="abs hero-text">
    <div class="l1">We provide best quality</div>
    <div class="head l2">Service for System Support,</div>
    <div class="head l3">Security and Cloud-based applications</div>
    <span class="btn">Let's Get Started</span>
  </div>
  <div class="abs hero-art" role="img" aria-label="Isometric illustration of cloud, servers, devices and security locks connected by circuit lines"></div>
</section>

<section class="abs about">
  <div class="abs ring"></div>
  <div class="abs art" role="img" aria-label="Illustration of a team around a laptop showing a video call"></div>
  <div class="abs copy">
    <h2 class="head">ABOUT <em>US</em></h2>
    <span class="mark"></span>
    <p class="body">We have provided web design, graphic design and application development solutions for a wide variety of industries. We are known for the quality of our work, affordable rates and our individual approach to each customer. Our company offers a wide variety of professional web solution and all this at very competitive prices!</p>
    <span class="btn">Read More</span>
  </div>
</section>

<section class="clients">
  <div class="abs copy">
    <h2 class="head">Our <em>Clients</em></h2>
    <span class="mark"></span>
    <p class="body">We undertake many projects from small businesses to large corporations. We are also extremely experienced in the long term support of comprehensive web based business systems providing first class development, maintenance, data entry services and enhancements. Click here to see more details.</p>
    <span class="btn">Read More</span>
  </div>
  <div class="abs arrow" style="left:599px;top:1462px"><svg width="10" height="10" viewBox="0 0 10 10"><path d="M7 1L3 5l4 4" fill="#999"/></svg></div>
  <div class="abs arrow" style="left:1053px;top:1462px"><svg width="10" height="10" viewBox="0 0 10 10"><path d="M3 1l4 4-4 4" fill="#999"/></svg></div>
  <div class="abs logo-card" style="left:680px;top:1351px">Halvorsen</div>
  <div class="abs logo-card" style="left:849px;top:1370px">Oakline</div>
  <div class="abs logo-card" style="left:680px;top:1465px">Brindle &amp; Co</div>
  <div class="abs logo-card" style="left:849px;top:1484px">Northcrest</div>
</section>

<section class="abs services">
  <div class="abs title centered"><h2 class="head">Our <em>Services</em></h2><div class="rule"><span class="mark"></span></div></div>
  <div class="abs arrow" style="left:76px;top:216px"><svg width="10" height="10" viewBox="0 0 10 10"><path d="M7 1L3 5l4 4" fill="#999"/></svg></div>
  <div class="abs arrow" style="left:1092px;top:216px"><svg width="10" height="10" viewBox="0 0 10 10"><path d="M3 1l4 4-4 4" fill="#999"/></svg></div>
  <div class="abs svc" style="left:128px;top:162px"><div class="disc"><svg width="64" height="64" viewBox="0 0 64 64" fill="none" stroke="#3b3f5c" stroke-width="2.5"><path d="M32 6l22 8v16c0 14-10 24-22 28C20 54 10 44 10 30V14z" fill="#f6b5b9"/><path d="M22 32l7 7 13-14" stroke="#e8313a"/></svg></div>Security &amp; Firewalls</div>
  <div class="abs svc" style="left:322px;top:162px"><div class="disc"><svg width="66" height="60" viewBox="0 0 66 60" fill="none" stroke="#3b3f5c" stroke-width="2.5"><rect x="4" y="8" width="40" height="28" rx="2"/><path d="M18 46h14M24 36v10"/><rect x="46" y="20" width="16" height="34" rx="2" fill="#f6b5b9"/><path d="M50 28h8M50 34h8"/></svg></div>Workstation<br>Support</div>
  <div class="abs svc on" style="left:516px;top:162px"><div class="disc"><svg width="54" height="64" viewBox="0 0 54 64" fill="none" stroke="#3b3f5c" stroke-width="2.5"><rect x="4" y="4" width="46" height="56" rx="4" fill="#f6b5b9"/><rect x="10" y="12" width="34" height="10" rx="2" fill="#fff"/><rect x="10" y="27" width="34" height="10" rx="2" fill="#fff"/><rect x="10" y="42" width="34" height="10" rx="2" fill="#fff"/></svg></div>Storage</div>
  <div class="abs svc" style="left:708px;top:162px"><div class="disc"><svg width="64" height="64" viewBox="0 0 64 64" fill="none" stroke="#3b3f5c" stroke-width="2.5"><path d="M16 34a12 12 0 0 1 2-24 16 16 0 0 1 30 4 10 10 0 0 1 0 20"/><rect x="22" y="22" width="20" height="36" rx="2" fill="#f6b5b9"/><path d="M27 30h10M27 37h10"/></svg></div>Networks &amp;<br>Databases</div>
  <div class="abs svc" style="left:902px;top:162px"><div class="disc"><svg width="64" height="56" viewBox="0 0 64 56" fill="none" stroke="#3b3f5c" stroke-width="2.5"><path d="M16 32a12 12 0 0 1 0-24 16 16 0 0 1 30 2 11 11 0 0 1 2 22z"/><path d="M22 32v10M32 32v14M42 32v10" stroke="#e8313a"/><circle cx="22" cy="45" r="3" fill="#f6b5b9"/><circle cx="32" cy="49" r="3" fill="#f6b5b9"/><circle cx="42" cy="45" r="3" fill="#f6b5b9"/></svg></div>Cloud</div>
</section>

<section class="news">
  <div class="abs title centered"><h2 class="head">Latest <em>News</em></h2><div class="rule"><span class="mark"></span></div></div>
  <div class="abs arrow" style="left:76px;top:2525px"><svg width="10" height="10" viewBox="0 0 10 10"><path d="M7 1L3 5l4 4" fill="#999"/></svg></div>
  <div class="abs arrow" style="left:1092px;top:2525px"><svg width="10" height="10" viewBox="0 0 10 10"><path d="M3 1l4 4-4 4" fill="#999"/></svg></div>
  <article class="abs card" style="left:141px">
    <div class="img" role="img" aria-label="Digital globe over a city at night" style="background:linear-gradient(160deg,#0d2a3f,#1d6d8f 55%,#7fb6c7)"><span class="date">21<small>NOV</small></span></div>
    <h3>Website: Quorvanta.net launches new website.</h3>
    <p>Our work is based on quality sales, customer and technical support services.</p>
    <span class="btn">Read More</span>
  </article>
  <article class="abs card" style="left:457px">
    <div class="img" role="img" aria-label="Padlock on a glowing circuit board" style="background:linear-gradient(135deg,#1c2f7a,#5a6fd0 50%,#d8573f)"><span class="date">21<small>NOV</small></span></div>
    <h3>Website: Quorvanta.net launches new website.</h3>
    <p>Our work is based on quality sales, customer and technical support services.</p>
    <span class="btn">Read More</span>
  </article>
  <article class="abs card" style="left:772px">
    <div class="img" role="img" aria-label="Business analyst working on a transparent data screen" style="background:linear-gradient(120deg,#e9f1f8,#9fb9d3 55%,#3b4f66)"><span class="date">21<small>NOV</small></span></div>
    <h3>Website: Quorvanta.net launches new website.</h3>
    <p>Our work is based on quality sales, customer and technical support services.</p>
    <span class="btn">Read More</span>
  </article>
</section>

<div class="abs faqband"></div>
<section class="abs faq">
  <h2 class="head">Frequently <em>Asked Questions</em></h2>
  <span class="mark"></span>
  <div class="acc-open">
    <div class="acc-head"><span>How much does a web site powered by Quorvanta.net cost?</span><span>–</span></div>
    <div class="acc-body">There are quite a few factors that are going to affect the ultimate cost of your web site. These factors include how many pages you are going to have, if you will sell products on your website, the graphic work involved, and how interactive your web site will be.</div>
  </div>
  <div class="acc-head acc-closed"><span>How long does it take to have a web site designed?</span><span>+</span></div>
</section>
<div class="abs divider"></div>
<section class="abs philo">
  <h2 class="head">Our <em>Philosophy</em></h2>
  <span class="mark"></span>
  <div class="box">
    <p class="body">As web developers, we understand that a powerful and functional web site is a vital component of modern day marketing for companies of today. This is why our web site development team work with all of our clients to ensure their web site design will deliver to their target market.</p>
    <span class="btn">Read More</span>
  </div>
</section>

<section class="contact">
  <div class="abs title centered"><h2 class="head">Quick <em>Contact</em></h2><div class="rule"><span class="mark"></span></div></div>
  <form class="abs form">
    <div class="field">First Name*</div>
    <div class="field">Last Name*</div>
    <div class="field">Email*</div>
    <div class="field"><span class="box-check"></span>I am not a robot</div>
    <div class="field msg">Message*</div>
  </form>
  <span class="abs btn send">Submit</span>
</section>

<footer class="abs footer">
  <div class="abs col" style="left:141px;top:68px;width:215px">
    <div class="logo">quorvanta.net<i></i></div>
    <p style="margin-top:10px">Quorvanta.net is an Australian based Software and Web Development Company that provides individual technology solutions and professional software for clients worldwide.</p>
  </div>
  <div class="abs col" style="left:410px">
    <h4>Contact <em>Details</em></h4>
    <div class="row"><span class="dot"></span>+61 7 5550 1842</div>
    <div class="row"><span class="dot"></span>+61 0400 555 318</div>
    <div class="row"><span class="dot"></span>info@quorvanta.com</div>
  </div>
  <div class="abs col" style="left:633px">
    <h4>Quick <em>Links</em></h4>
    <div>Home</div><div>Our Services</div><div>Our Clients</div><div>Contact Us</div>
  </div>
  <div class="abs col" style="left:776px">
    <h4>Subcribe <em>to your newletter</em></h4>
    <div>You can be always up to date with our company news</div>
    <div class="news-form"><span>Enter your Email*</span><b>Submit</b></div>
    <div class="social" style="margin-top:14px"><span></span><span></span><span></span></div>
  </div>
  <div class="abs copy">© 2019 quorvanta. All Right Reserved.</div>
</footer>

</body>
</html>
```